new roofing company card

New primary business card for roofing company.

Industry/Entity Type

Residential roofing/Specializing in Asphalt and Standing seam metal roofing

Contact Information for Business Card

Phone number is: 484 672 1058 Email: support@fennridgeroofworks.com website: www.fennridgeroofworks.com

Colors
EB3D1F
EC4F4E
F09395
F8D3D4
FCEDEE

```html
<!DOCTYPE html>
<html lang="en">
<head>
<meta charset="utf-8">
<title>Fennridge Roofworks – Business Card</title>
<link href="https://fonts.googleapis.com/css2?family=Arimo:wght@400;700&display=swap" rel="stylesheet">
<style>
  :root {
    --stage: #3d3d3d;
    --card-white: #ffffff;
    --card-dark: #2b2b2b;
    --pattern-dark: #262626;
    --ink: #1f1f1f;
    --ink-soft: #4a4a4a;
    --rule: #d6d6d6;
    --brand-red: #c8281e;
    --mark-light: #e9e9e9;
  }
  * { box-sizing: border-box; margin: 0; padding: 0; }
  html, body {
    width: 1200px;
    height: 803px;
    overflow: hidden;
    background: var(--stage);
    font-family: "Arimo", Arial, sans-serif;
  }
  .stage {
    position: relative;
    width: 1200px;
    height: 803px;
    display: flex;
    align-items: center;
    justify-content: center;
    gap: 40px;
  }
  .card {
    position: relative;
    width: 540px;
    height: 310px;
    border-radius: 22px;
    overflow: hidden;
    box-shadow: 0 18px 40px rgba(0,0,0,0.35);
  }

  /* Front */
  .card--front {
    background: var(--card-white);
    border-bottom: 3px solid var(--brand-red);
  }
  .brand {
    position: absolute;
    top: 40px;
    right: 42px;
    display: flex;
    align-items: center;
    gap: 12px;
  }
  .brand__square {
    width: 22px;
    height: 22px;
    background: var(--brand-red);
  }
  .brand__name {
    font-weight: 700;
    font-size: 26px;
    line-height: 1.05;
    letter-spacing: 0.06em;
    color: var(--ink);
    text-transform: uppercase;
  }
  .holder {
    position: absolute;
    left: 42px;
    bottom: 84px;
  }
  .holder__name {
    font-weight: 700;
    font-size: 24px;
    letter-spacing: 0.02em;
    color: var(--ink);
    text-transform: uppercase;
  }
  .holder__title {
    margin-top: 4px;
    font-size: 14px;
    color: var(--brand-red);
  }
  .contact {
    position: absolute;
    left: 42px;
    right: 42px;
    bottom: 32px;
    padding-top: 12px;
    border-top: 1px solid var(--rule);
    font-size: 12px;
    color: var(--ink-soft);
    white-space: nowrap;
  }
  .contact__sep { margin: 0 6px; }

  /* Back */
  .card--back {
    background: var(--card-dark);
    border-left: 2px solid var(--brand-red);
    border-bottom: 2px solid var(--brand-red);
  }
  .back__pattern {
    position: absolute;
    inset: 0;
    background: linear-gradient(160deg, var(--card-dark), var(--pattern-dark));
  }
  .back__mark {
    position: absolute;
    right: 44px;
    bottom: 92px;
    font-weight: 700;
    font-size: 13px;
    letter-spacing: 0.06em;
    color: var(--mark-light);
    text-transform: uppercase;
  }
</style>
</head>
<body>
  <main class="stage">
    <section class="card card--front" aria-label="Business card front">
      <div class="brand">
        <span class="brand__square" aria-hidden="true"></span>
        <span class="brand__name">Fennridge<br>Roofworks</span>
      </div>
      <div class="holder">
        <p class="holder__name">Dana Whitlock</p>
        <p class="holder__title">President</p>
      </div>
      <p class="contact">
        <span>484 672 1058</span><span class="contact__sep">|</span><span>support@fennridgeroofworks.com</span><span class="contact__sep">|</span><span>www.fennridgeroofworks.com</span>
      </p>
    </section>

    <section class="card card--back" aria-label="Business card back">
      <div class="back__pattern" role="img" aria-label="Tone-on-tone repeating monogram pattern across the dark card back"></div>
      <p class="back__mark">Fennridge Roofworks</p>
    </section>
  </main>
</body>
</html>
```